Eastward keel catch

Hi everyone,
I’m operating a fishing boat targeting sought after deep water fish species off the southern coast of wa, where the product is sold from the boat directly to restaurants around the region. We fish with rods and not nets ensuring the fish are caught in an eco friendly manner maintaining longevity of the industry. This fishery takes place along a rugged coastline and wild oceans where conditions are not always favourable. Hoping for a design that can encompass these elements and also the care taken during harvest of the product ensuring quality of the fish and freshest fillets. I’ve attached photos of some targeted species, blue eye trevalla and dhufish, nannigai and pink snapper which would be nice to include
Thanks marcus

Target Market(s)

Restaurants/ seafood processors

Contact Information for Business Card

Top quality line caught scalefish, sustainably sourced from the pristine waters of south west WA
Contact marcus holt 0417586204

Requirements
Must have
• Catchy design yet simple
Appealing and promote values of business
-premium quality and freshness
-minimal impact on environment
Nice to have
• The wa dhufish incorporated in the logo. Kestrelbaitco.example have a few good examples as theirs

```html
<!DOCTYPE html>
<html lang="en">
<head>
<meta charset="UTF-8">
<title>Eastward Keel Catch – Business Card</title>
<link rel="stylesheet" href="https://fonts.googleapis.com/css2?family=EB+Garamond:wght@400;500&display=swap">
<style>
  :root {
    --page-bg: #e9e6e3;
    --card-white: #f7f7f5;
    --navy: #0c1a47;
    --ink: #14224f;
    --paper-text: #f4f4f2;
    --fish-red: #d8482e;
    --fish-salmon: #e39a7c;
    --fish-slate: #5b6478;
    --fish-olive: #6d6a4a;
    --fish-mauve: #8a6f86;
  }
  * { margin: 0; padding: 0; box-sizing: border-box; }
  html, body {
    width: 1200px; height: 800px; overflow: hidden;
    background: var(--page-bg);
  }
  body {
    display: flex; align-items: center; justify-content: center; gap: 40px;
    font-family: "EB Garamond", Garamond, serif;
  }
  .card {
    position: relative;
    width: 540px; height: 300px;
    box-shadow: 0 10px 28px rgba(40, 30, 20, 0.18);
  }
  .card--front { background: var(--card-white); color: var(--ink); }
  .card--back { background: var(--navy); color: var(--paper-text); }

  .dots { position: absolute; display: flex; gap: 14px; }
  .dots--vertical { flex-direction: column; }
  .dot { width: 3px; height: 3px; border-radius: 50%; background: currentColor; }

  .tagline { position: absolute; left: 34px; top: 36px; line-height: 1; }
  .tagline__small { display: block; font-size: 12px; margin: 3px 0 2px; letter-spacing: 0.02em; }
  .tagline__large { display: block; font-size: 27px; font-weight: 500; }

  .contact { position: absolute; right: 38px; top: 110px; text-align: left; }
  .contact__label { font-size: 13px; letter-spacing: 0.06em; }
  .contact__name { font-size: 32px; font-weight: 500; line-height: 1; margin: 2px 0 4px; }
  .contact__phone { font-size: 12px; letter-spacing: 0.12em; }

  .brand { position: absolute; line-height: 0.88; font-weight: 500; }
  .brand__line { display: block; }
  .brand__line--indent { padding-left: 0.55em; }
  .card--front .brand { left: 130px; bottom: 40px; font-size: 40px; }
  .card--back .brand { left: 300px; top: 118px; font-size: 34px; }

  .fish-art {
    position: absolute; left: 110px; top: 78px; width: 180px; height: 140px;
    border-radius: 50%;
    background:
      radial-gradient(ellipse at 60% 30%, var(--fish-red) 0 22%, transparent 42%),
      radial-gradient(ellipse at 90% 22%, var(--fish-salmon) 0 16%, transparent 34%),
      radial-gradient(ellipse at 22% 32%, var(--fish-slate) 0 18%, transparent 36%),
      radial-gradient(ellipse at 62% 70%, var(--fish-olive) 0 18%, transparent 36%),
      radial-gradient(ellipse at 24% 76%, var(--fish-mauve) 0 18%, transparent 36%);
    opacity: 0.9;
  }
</style>
</head>
<body>

  <section class="card card--front" aria-label="Business card front">
    <p class="tagline">
      <span class="tagline__small">Top quality line</span>
      <span class="tagline__large">caught scalefish,</span>
      <span class="tagline__small">sustainably sourced from the pristine waters of</span>
      <span class="tagline__large">south west WA.</span>
    </p>

    <div class="contact">
      <p class="contact__label">Contact</p>
      <p class="contact__name">Marcus Holt</p>
      <p class="contact__phone">0417586204</p>
    </div>

    <div class="dots dots--vertical" style="right: 30px; top: 26px;">
      <span class="dot"></span><span class="dot"></span><span class="dot"></span>
    </div>
    <div class="dots dots--vertical" style="left: 92px; top: 150px;">
      <span class="dot"></span><span class="dot"></span><span class="dot"></span>
    </div>

    <h1 class="brand">
      <span class="brand__line">Eastward</span>
      <span class="brand__line brand__line--indent">Keel Catch</span>
    </h1>
  </section>

  <section class="card card--back" aria-label="Business card back">
    <div class="dots dots--vertical" style="left: 30px; top: 110px;">
      <span class="dot"></span><span class="dot"></span><span class="dot"></span>
    </div>

    <div class="fish-art" role="img" aria-label="Illustration of five target fish: blue eye trevalla, nannygai, pink snapper, dhufish and a groper, swimming as a school"></div>

    <h2 class="brand">
      <span class="brand__line">Eastward</span>
      <span class="brand__line brand__line--indent">Keel Catch</span>
    </h2>

    <div class="dots" style="right: 40px; bottom: 100px; gap: 22px;">
      <span class="dot"></span><span class="dot"></span><span class="dot"></span><span class="dot"></span><span class="dot"></span>
    </div>
  </section>

</body>
</html>
```